Brochure Design Project

Need a new look. Customer wants to update 10 year old literature. Very similar "text content" and color scheme only. Need a new modern look. Clean fonts...maybe distressed fonts. Nice salon. Would like brochure to be consistent with their decor...possibly "curvey" graphics maybe simple die-cut if cost effective to produce. Use your imagination! Showed them some pixel harbor work that they liked the look of and I will share these details so you have a feel for the type of work we are looking for.

Reason: My customer has reviewed the art submissions and though she likes the ideas presented, she has indicated that she needs to stay more consistent with some other collateral which means she would prefer a more mono-chromatic (maybe two or three colors but not a full color glossy brochure. Keeping in mind that she would like a matte look please offer design selections. She has sent me some images of the other collateral she would possibly like to coordinate with which I can send via email upon request.

Target Market(s)

Salon Patrons

Industry/Entity Type

Salon

Requirements
Must have
• Packaged InDesign file upon completion so we can edit down the line(update prices etc.) High Res PDF with marks and bleeds. Must fit into No. 10 envelope(4.125" x 9.5") once folded...I am thinking 9x16 but am open to ideas.
Should not have
• photos...or limit

```html
<!DOCTYPE html>
<html lang="en">
<head>
<meta charset="utf-8">
<title>Lumea Salon Spa – Brochure</title>
<link href="https://fonts.googleapis.com/css2?family=Open+Sans:ital,wght@0,400;0,600;0,700;0,800;1,700;1,800&display=swap" rel="stylesheet">
<style>
:root{
  --lime:#8dc63f;
  --lime-light:#c5e17a;
  --lime-pale:#e4f1c3;
  --green:#3d8b22;
  --green-dark:#2c6a16;
  --charcoal:#3a3a3a;
  --ink:#2b2b2b;
  --muted:#555;
  --white:#fff;
  --paper:#fbfbf8;
}
*{box-sizing:border-box;margin:0;padding:0}
html,body{width:1068px;height:1200px;overflow:hidden;background:var(--white)}
body{font-family:"Open Sans",Arial,sans-serif;color:var(--ink);font-size:7.4px;line-height:1.28;position:relative}
.spread{position:absolute;left:47px;width:973px;overflow:hidden;background:var(--paper)}
.spread--outside{top:47px;height:546px;border-top:10px solid var(--charcoal);border-bottom:8px solid var(--charcoal)}
.spread--inside{top:607px;height:553px;border-top:14px solid var(--charcoal)}
.panel{position:absolute;top:0;bottom:0;overflow:hidden;padding:10px 12px}
.p1{left:0;width:280px}
.p2{left:280px;width:206px;background:linear-gradient(180deg,var(--lime-light),var(--lime) 70%)}
.p3{left:486px;width:220px;background:var(--white)}
.p4{left:706px;width:267px;background:linear-gradient(200deg,var(--lime) 0%,var(--lime-light) 40%,var(--white) 70%)}
h2.packages{font-size:15px;font-weight:700;color:var(--ink);margin-bottom:4px}
.note{font-size:6.8px;color:var(--muted);margin-bottom:6px}
.break{font-size:15px;font-style:italic;font-weight:800;color:var(--green);margin:4px 0 3px}
.pkg h3{font-size:7.6px;font-weight:700;text-transform:uppercase;color:var(--ink);margin-top:5px}
.pkg p{font-size:6.9px}
.photo{display:block}
.photo--massage{position:absolute;right:12px;top:98px;width:92px;height:62px;background:linear-gradient(135deg,#e9d8c4,#b68e6e)}
.photo--massage2{position:absolute;right:12px;bottom:12px;width:120px;height:72px;background:linear-gradient(135deg,#f1e5d8,#c99a7a)}
.create{position:absolute;left:12px;bottom:12px;width:128px;font-size:7px}
.create h3{font-size:7.6px;font-weight:700;margin-bottom:2px}
.about-title{display:flex;align-items:center;gap:6px;font-size:15px;font-weight:600;color:var(--ink);margin-bottom:6px}
.dot{width:14px;height:14px;border-radius:50%;background:var(--white)}
.policy{display:grid;grid-template-columns:62px 1fr;gap:2px 6px;font-size:6.8px}
.policy dt{font-weight:700;text-align:right;text-transform:uppercase}
.policy dd{margin-bottom:5px}
.featured{position:absolute;right:10px;top:336px;text-align:right;font-style:italic;font-weight:800;font-size:9.4px;line-height:1.35;color:var(--white);text-transform:uppercase;z-index:2;text-shadow:0 0 2px rgba(0,0,0,.25)}
.photo--stones{position:absolute;left:0;right:0;bottom:0;height:120px;background:radial-gradient(ellipse at 45% 70%,#8a7664,#c9b49c 45%,transparent 75%),linear-gradient(180deg,transparent,#c7dc98)}
.hours{position:absolute;left:12px;top:6px;width:96px;height:204px;background:var(--white);border:2px solid var(--lime);border-radius:0 0 8px 8px;text-align:center;font-size:6.8px}
.hours__tag{background:var(--green);color:var(--white);font-weight:700;padding:5px 0;font-size:7.4px;text-transform:uppercase}
.hours__list{padding:8px 2px;line-height:1.7;white-space:nowrap}
.hours__dir{background:var(--green);color:var(--white);font-weight:700;font-size:6.4px;padding:2px 0;margin:2px 16px;border-radius:3px}
.hours__text{padding:4px 6px;font-size:6px;text-align:left;color:var(--muted)}
.team{position:absolute;left:116px;right:8px;top:10px;font-size:6.9px;text-align:center;color:var(--ink)}
.team p{margin-bottom:6px}
.photo--face{position:absolute;left:116px;top:150px;width:96px;height:70px;background:linear-gradient(135deg,#f5e6dc,#d8b6a0)}
.care{position:absolute;left:12px;right:10px;top:232px;font-size:6.8px}
.care p{margin-bottom:6px}
.brand{font-weight:700;color:var(--green-dark);display:flex;align-items:center;gap:5px}
.brand__mark{width:12px;height:12px;border-radius:50%;background:var(--lime)}
.brand--small{position:absolute;left:70px;top:432px;font-size:13px}
.contact-small{position:absolute;left:12px;right:10px;top:452px;text-align:center;font-size:6.8px;line-height:1.5}
.address{position:absolute;left:12px;right:10px;bottom:14px;text-align:right;font-size:6.8px;line-height:1.5}
.brand--cover{position:absolute;right:18px;top:54px;font-size:26px;flex-direction:column;align-items:flex-end;gap:2px}
.brand--cover .brand__mark{width:26px;height:26px;background:var(--green)}
.cover-text{position:absolute;left:28px;right:16px;top:178px;text-align:center;font-size:7.4px;line-height:1.62}
.photo--relax{position:absolute;left:0;right:0;top:300px;height:180px;background:linear-gradient(160deg,#ffffff 0%,#efe4dc 45%,#d6bba8 100%)}
.cover-contact{position:absolute;left:16px;bottom:10px;font-size:6.8px;line-height:1.5}
.ip{position:absolute;top:0;bottom:24px;overflow:hidden;padding:0 10px 6px}
.i1{left:0;width:280px;background:var(--paper)}
.i2{left:280px;width:206px;background:var(--white)}
.i3{left:486px;width:220px;background:var(--paper)}
.i4{left:706px;width:267px;background:var(--white)}
.bar{background:var(--lime);color:var(--white);font-weight:700;font-size:11px;text-transform:uppercase;padding:3px 10px;margin:6px -10px 4px}
.bar--top{margin-top:0}
.bar--dark{background:var(--green)}
.item h4{font-size:7px;font-weight:700;text-transform:uppercase;margin-top:5px}
.item p{font-size:6.7px;line-height:1.3}
.photo--stone-small{position:absolute;right:12px;bottom:6px;width:58px;height:44px;background:radial-gradient(ellipse at 50% 65%,#7c6a5a,#c8b39a 50%,transparent 75%)}
.footer{position:absolute;left:0;right:0;bottom:0;height:24px;background:var(--charcoal);color:var(--white);font-weight:700;font-size:9px;display:flex;align-items:center}
.footer span:first-child{padding-left:290px}
.footer span:last-child{margin-left:auto;padding-right:110px}
</style>
</head>
<body>

<section class="spread spread--outside">
  <div class="panel p1">
    <h2 class="packages">Spa Packages</h2>
    <p class="note">*All times are approximate. Dressing time and a complimentary foot soak are included.</p>
    <div class="pkg"><p style="padding-left:30px">Express Facial and Half Hour Massage,<br>*Approximately 1 1/2 hours $100</p></div>
    <div class="break">take a break...</div>
    <div class="pkg" style="width:168px">
      <h3>Couples Escape</h3><p>Two people receive a Full Body Massage in our couples suite. *Approximately 1 1/2 hours $140</p>
      <h3>Taste of Pampering</h3><p>Half-Hour Massage, Express Facial and Pedicure. *Approximately 2 1/2 hours $154</p>
      <h3>Lumea Afternoon Getaway</h3><p>Scrub or Wrap, Full Body Massage, Customized Facial and Lunch. *Approximately 4 hours $190</p>
      <h3>Lumea Mental Retreat</h3><p>Scrub, Wrap, Full Body Massage, Customized Facial and Lunch. *Approximately 4 hours $240</p>
      <h3>Lumea Relaxation Vacation</h3><p>Scrub, Wrap, Full Body Massage, Customized Facial, Spa Manicure, Spa Pedicure and Lunch. *Approximately 5 hours $338</p>
    </div>
    <div class="pkg">
      <h3>Our Afternoon Rendezvous</h3><p>Two people enjoy a Scrub or Wrap, Full Body Massage, Customized Facial and Lunch. *Approximately 3 1/2 hours $380</p>
      <h3>Imagine the Experience</h3><p>Scrub, Wrap, Full Body Massage, Customized Facial, Hot Stone Massage, Spa Manicure, Spa Pedicure, Hair Cut and Style, and Lunch. *Approximately 7 hours $465</p>
    </div>
    <div class="photo photo--massage" role="img" aria-label="Photo of a guest receiving a back massage"></div>
    <div class="create"><h3>CREATE YOUR OWN EXPERIENCE</h3>Choose any combination of your favorite spa experiences and let us do the rest to make it a day to remember. A value of $160 or more includes a complimentary lunch during your visit.</div>
    <div class="photo photo--massage2" role="img" aria-label="Photo of a relaxing spa massage with flower petals"></div>
  </div>

  <div class="panel p2">
    <div class="about-title"><span class="dot"></span>About us</div>
    <dl class="policy">
      <dt>Children</dt><dd>For insurance and safety reasons, children are not permitted in any service area of the salon or spa unless having a service performed.</dd>
      <dt>Cell Phones</dt><dd>For the courtesy of our guests we ask that your cell phone be turned to vibrate or off. Cell phones are not permitted in the spa.</dd>
      <dt>Pricing</dt><dd>All prices are subject to change without notice.</dd>
      <dt>Cancellation</dt><dd>At Lumea salon and spa, we require a 24-hour cancellation notice.</dd>
      <dt>Multiple Services</dt><dd>For multiple services, bridal parties and spa packages, we do require a credit card number for confirmation. In the event you miss your scheduled appointment, charges will be applied to your card.</dd>
      <dt>Retail Returns</dt><dd>No cash refunds. Exchange only on all retail items excluding brushes and makeup which are non-returnable.</dd>
      <dt>Gift Certificates</dt><dd>Gift certificates are available in any denomination. For your convenience, gift certificates can be purchased on line at www.lumeasalonspa.com. All gift certificates are non-refundable and carry their value for one year.</dd>
    </dl>
    <div class="featured">Couples Escape<br>Lumea Retreat<br>Hot Stone Massage<br>Taste of Pampering<br>Our Afternoon Rendezvous<br>Create Your Own Experience<br>Our Afternoon Rendezvous</div>
    <div class="photo photo--stones" role="img" aria-label="Photo of stacked spa stones with a pink flower"></div>
  </div>

  <div class="panel p3">
    <div class="hours">
      <div class="hours__tag">Salon Hours</div>
      <div class="hours__list">Monday &amp;<br>Wednesday 9-6<br>Tuesday &amp; Thursday 9-9<br>Friday 9-7<br>Saturday 9-5</div>
      <div class="hours__dir">DIRECTIONS</div>
      <div class="hours__text">From Northfield take Route 75 to the Maplewood exit. Left off the exit. On the right, less than a 1/2 mile. From Riverton or Eastbrook take Route 71 to Maplewood exit, right off the exit, the salon is on the right.</div>
    </div>
    <div class="team">
      <p>We are proud to have a team of wonderful people who are dedicated to self-growth, continued education and who have a strong desire to make people look and feel better. When you look good, you feel good.</p>
      <p>Our staff is committed to serving our guests as a team. We encourage trying our various technicians in order to enjoy all of their wonderful talents and ideas.</p>
    </div>
    <div class="photo photo--face" role="img" aria-label="Photo of a relaxed spa guest"></div>
    <div class="care">
      <p>Communication is the key to a successful relationship with our clients. If at any time you are uncomfortable or dissatisfied in any way, we promise to make every effort to remedy the situation. Your opinions and comments are vital to the growth and success of our business and are greatly appreciated. If, for any reason, you are unhappy with a Lumea product, we will gladly exchange it with an equal product more suitable to your needs.</p>
      <p>To ensure you get the appointment time you most desire, we encourage you to book your next appointment before leaving.</p>
      <p>In the event that you cannot make your scheduled appointment we ask that you give us a 24-hour cancellation notice so that we may accommodate another Lumea salon and spa client.</p>
    </div>
    <div class="brand brand--small"><span class="brand__mark"></span>Lumea Salon Spa</div>
    <div class="contact-small">www.lumeasalonspa.com<br>hello@lumeasalonspa.com</div>
    <div class="address">2190 Alder Crest Road, Maplewood, Kentucky 40999 USA<br>555 lumea (586 3200)</div>
  </div>

  <div class="panel p4">
    <div class="brand brand--cover"><span class="brand__mark"></span>Lumea Salon Spa</div>
    <div class="cover-text">At Lumea salon and spa we are dedicated to making every visit a positive experience. Whether you are here for a day of pampering or for your regular salon appointment, our staff of experienced professionals are dedicated to meeting your every need. Escape the stresses of life and discover a new environment of relaxation and beauty.</div>
    <div class="photo photo--relax" role="img" aria-label="Photo of a woman resting peacefully in a spa robe"></div>
    <div class="cover-contact">555 lumea (586 3200)<br>hello@lumeasalonspa.com<br>www.lumeasalonspa.com</div>
  </div>
</section>

<section class="spread spread--inside">
  <div class="ip i1">
    <div class="bar bar--top">Massage</div>
    <div class="item">
      <h4>Swedish Massage</h4><p>Reduces and relieves stress and muscle tension. Induces deep relaxation and improves circulation and range of motion. Target Area (approx 25 min) $50 · Full Body (approx 50 min) $70 · Extended Full Body (approx 80 min) $120</p>
      <h4>Prenatal Massage</h4><p>Relieves stress on weight bearing joints and induces deep relaxation. Always consult your OB/GYN. Target Area $50 · Full Body $70</p>
      <h4>Seated Massage</h4><p>The perfect solution for neck and shoulder pain. An abbreviated massage targeted to pressure points of the scalp, neck and shoulders. $25</p>
      <h4>Four Handed Massage... (our signature treatment)</h4><p>The ultimate relaxation experience. Have two of our skilled therapists work on you simultaneously. Target (approx 30 min) $100 · Full body (approx 60 min) $140</p>
      <h4>Hot Stone Massage</h4><p>This therapeutic treatment incorporates hot stones with classic massage movements. $85 (approx 60 min)</p>
      <h4>Deep Tissue Massage</h4><p>Goes beyond Swedish Relaxation Massage by going deeper into the tissue or muscles that are responsible for holding chronic pain patterns. $90 (approx 60 min)</p>
      <h4>Scalp Massage (15 min) $20 &nbsp; Foot Massage (15 min) $20</h4>
    </div>
    <div class="bar">Body Treatments</div>
    <div class="item">
      <h4>Body Scrubs and Wraps</h4><p>We offer a full line of customized body scrubs and wraps. These treatments help to exfoliate, remineralize, rehydrate and detoxify. After a consultation with your trained therapist it will be determined which treatment will best suit your needs. Scrub $50 and up · Wrap $50 and up · Scrub &amp; Wrap $100 and up</p>
      <p>This treatment is like a facial for your back. It will help refine the texture and improve the appearance of the skin on the back. This is a must for anyone wearing a backless dress. $55</p>
      <h4>Sinus Treatment</h4><p>This treatment involves steam and localized massage to give you relief from sinus pressure and help encourage the sinuses to drain. $50</p>
    </div>
  </div>

  <div class="ip i2">
    <div class="bar bar--top">Facials</div>
    <div class="item">
      <h4>Express Facial</h4><p>This facial includes cleansing, steaming, exfoliation, pressure point massage and a 5 minute maintenance treatment mask. $50</p>
      <h4>Teen Facial</h4><p>This is an express facial with a very thorough skin care consultation to address the challenges faced by the teen years. $55</p>
      <h4>Customized Facial</h4><p>This facial is customized to meet any skin care needs you may have. Includes cleansing, steaming, exfoliation on the décolleté, neck and shoulders. Includes a detox massage, pressure point massage and relaxation massage, a 10-15 minute treatment mask, hand, arm, foot and leg massage. Women $70 · Men with shave consultation $70 · Extractions $10</p>
      <h4>Natural Peels</h4><p>Peels are a much deeper form of exfoliation. They go one step beyond a customized facial without the redness and dehydration of some other peeling treatments. These peels are done in conjunction with a Customized Facial. (approx. 80 min) Royal Peel $110 · Algae Peel $95</p>
      <h4>Pumpkin Facial</h4><p>Granuals and enzymes that encourage the removal of skin cell build up without stress or irritation of the skin. $85</p>
      <h4>Radiance Renewal Facial</h4><p>Incorporating retinols, glycolics and lactic acids to improve skin tone and texture. $75</p>
      <h4>Skin Brightening Facial</h4><p>Helps to improve dull or uneven skin tone, sun and environmentally damaged, mature and hyperpigmented skin. $85</p>
      <h4>Microdermabrasion</h4><p>Renew and revitalize your skin with this non-invasive exfoliating procedure. This type of skin resurfacing can be performed in an individual session, yet provides optimum results when performed in a series. Call for pricing</p>
      <h4>Chemical Exfoliation / Peels</h4><p>Chemical exfoliation can help improve many skin conditions, from acne and hyperpigmentation to dull sun damaged aging skin. Enzyme, Lactic, Salicylic, Glycolic 30% &amp; 80%, Modified Jessner &amp; TCA. $85 – $150 (Series pricing available). Must have consultation before booking peel. (15 min.) NO CHARGE</p>
    </div>
  </div>

  <div class="ip i3">
    <div class="item" style="padding-top:4px">
      <h4>Hot Stone Facial</h4><p>Enjoy the benefits of the Customized Facial enhanced by the use of hot and cold stones used during the massage. $85</p>
    </div>
    <div class="bar bar--dark">Body Waxing</div>
    <div class="item">
      <h4>Full Body Waxing</h4><p>(For all waxing services you must have 2-3 weeks growth)<br>Lip/Brow/Chin/Sideburns/Stomach $15 each area and up<br>Bikini/Under Arms/Forearms start at $25 each service<br>Full Legs/Men's Back/Men's Chest $50 each service<br>Half Legs/Full Arms $30 each service<br>Brazilian Wax $75 and up</p>
    </div>
    <div class="bar">Hair</div>
    <div class="item">
      <p>All services are a la carte.</p>
      <h4>Cuts</h4><p>Women $24 and up · Men $21 and up · Student $21 and up<br>Child (0-11) $15 and up · Bang Trim $15 and up</p>
      <h4>Style</h4><p>Formal $45 and up · Bride $55 and up · Casual $18 and up</p>
      <h4>Foil: Full $55 and up · Half $45 and up · Face $35 and up</h4>
      <h4>Color: All Over Color $40 and up</h4>
      <h4>Perm: Regular $65 and up · Relaxers: Regular $75 and up</h4>
    </div>
    <div class="bar bar--dark">Hair Extensions</div>
    <div class="item">
      <h4>Human Hair Extensions</h4><p>We offer natural human hair extensions that last 3-6 months. They attach to small strands of your own hair. Whether you just want to add length, thickness or highlights we have the solution. All our extension specialists have gone through extensive training and are certified by the manufacturer.</p>
      <h4>Hair Pieces</h4><p>We offer hair pieces and Jade Summers clip-in hair pieces for that quick and easy total change. They are great for: weddings, proms, special occasions, or everyday. Maybe you are looking to add thickness or a highlighting affect to your own hair; we carry human hair and synthetic hairpieces so you can choose.</p>
      <h4>Eyelash Extensions</h4><p>Eyelash extensions are a revolutionary new way to add length and thickness to your current lashes; they are semi-permanent individual eyelash extensions not your traditional false eyelash strips. They will look and feel like your own lashes.<br>Call for consultation and pricing</p>
    </div>
  </div>

  <div class="ip i4">
    <div class="bar bar--top bar--dark">Makeup</div>
    <div class="item">
      <p>Includes complimentary mascara</p>
      <h4>Application: $40 &nbsp; application with lesson: $60</h4>
      <h4>Eyelash and Eyebrow Tinting: Call for pricing</h4>
    </div>
    <div class="bar">Hands and Feet</div>
    <div class="item">
      <h4>Ultimate Pedicure</h4><p>Pedicure performed in private spa room. Includes skin mask, hand and arm massage, scalp massage, and foot and leg massage. $75 · French $80</p>
      <h4>Manicure</h4><p>Includes filing and shaping of the nails, trimming cuticles, massage of the hand and polish. $22-$24 · French $27 and up</p>
      <h4>Spa Manicure</h4><p>Includes filing and shaping of the nails, trimming cuticles, exfoliation, massage of the hand, hot towel treatment or paraffin treatment and polish. $32-$34 · French $37 and up</p>
      <h4>Pedicure</h4><p>After soaking your feet in the whirlpool, allow us to file and shape the nails, trim the cuticles, rid you of excess dead skin and callouses, massage the feet and polish the nails. $52-$54 · French $57 and up</p>
      <h4>Spa Pedicure</h4><p>In addition to everything in the regular pedicure receive an exfoliation and hot towel treatment or paraffin treatment. $62-$64 · French $67 and up</p>
      <h4>Toes to Go</h4><p>After soaking your feet in the whirlpool, allow us to file and shape the nails, trim the cuticles and polish the nails. $35 · French $40 and up</p>
      <h4>Polish Change</h4><p>Tired of that color but not ready for another manicure just yet... Let us change your polish to improve the look. Fingers $10 · Toes $15 + $5 for French</p>
      <h4>Buff/Polish</h4><p>Includes filing and shaping of the nails, buffing and polish. Fingers $15 · Toes $20 + $5 for French</p>
      <h4>Artificial Nails</h4><p>Full Set $40 and up · Fill In $30 and up · Nail Wrap $50 · Repair $6 and up · Soak Off $15</p>
      <h4>Nail Art:</h4><p>Consult with a nail technician for specific pricing. $5 and up</p>
    </div>
    <div class="photo photo--stone-small" role="img" aria-label="Photo of spa stones with a pink flower"></div>
  </div>

  <div class="footer"><span>Email: hello@lumeasalonspa.com</span><span>www.lumeasalonspa.com</span></div>
</section>

</body>
</html>
```